Business Card Design Project

We need a double-sided business card design for our e-commerce company. Be as creative as you can.

Reason: Change of logo

Target Market(s)

Business owners

Industry/Entity Type

E-Commerce

Requirements
Must have
• Name (editable)
Mobile number -editable
www.trizvo.com - MUST STAND OUT ALONE
Office address:
27 Pellow Road
#09-04 Corbell Tower
Singapore 058214

```html
<!DOCTYPE html>
<html lang="en">
<head>
<meta charset="utf-8">
<title>Trizvo Business Card</title>
<link href="https://fonts.googleapis.com/css2?family=Questrial&display=swap" rel="stylesheet">
<style>
  :root {
    --backdrop: #ebebeb;
    --card: #070707;
    --brand-orange: #f47a20;
    --brand-blue: #2e8fd8;
    --text-light: #f2f2f2;
    --text-muted: #bdbdbd;
    --rule: #6a6a6a;
  }
  * { margin: 0; padding: 0; box-sizing: border-box; }
  html, body {
    width: 1200px;
    height: 750px;
    overflow: hidden;
    background: var(--backdrop);
    font-family: "Questrial", sans-serif;
  }
  .card-set {
    position: absolute;
    top: 225px;
    left: 50px;
    display: flex;
    gap: 60px;
  }
  .card {
    position: relative;
    width: 520px;
    height: 300px;
    background: var(--card);
    border-radius: 4px;
    box-shadow: 0 10px 24px rgba(0,0,0,0.18);
  }
  .wordmark {
    display: flex;
    align-items: center;
    gap: 8px;
    color: var(--brand-orange);
    font-weight: 400;
    letter-spacing: 1px;
  }
  .wordmark-dot {
    border-radius: 50%;
    background: var(--brand-blue);
  }
  /* Front */
  .card-front {
    display: flex;
    align-items: center;
    justify-content: center;
  }
  .card-front .wordmark { font-size: 76px; }
  .card-front .wordmark-dot { width: 16px; height: 16px; margin-top: 28px; }
  /* Back */
  .card-back { display: flex; }
  .contact-panel {
    width: 330px;
    padding: 40px 0 36px 36px;
    display: flex;
    flex-direction: column;
    justify-content: space-between;
    color: var(--text-light);
  }
  .person-name { font-size: 27px; line-height: 1.1; }
  .person-role { font-size: 13px; color: var(--text-muted); margin-top: 4px; }
  .contact-phone { font-size: 13px; margin-top: 22px; letter-spacing: 0.5px; }
  .office-address {
    font-style: normal;
    font-size: 13px;
    line-height: 1.55;
    color: var(--text-light);
  }
  .divider {
    width: 1px;
    margin: 26px 0;
    background: var(--rule);
  }
  .brand-panel {
    flex: 1;
    display: flex;
    flex-direction: column;
    align-items: center;
    justify-content: center;
    gap: 26px;
  }
  .brand-panel .wordmark { font-size: 36px; }
  .brand-panel .wordmark-dot { width: 9px; height: 9px; margin-top: 14px; }
  .website {
    font-size: 14px;
    color: var(--text-light);
    letter-spacing: 0.5px;
  }
</style>
</head>
<body>
  <main class="card-set">
    <section class="card card-front" aria-label="Card front">
      <div class="wordmark"><span>trizvo</span><span class="wordmark-dot"></span></div>
    </section>

    <section class="card card-back" aria-label="Card back">
      <div class="contact-panel">
        <div class="identity">
          <p class="person-name">Alex Tan</p>
          <p class="person-role">Manager</p>
          <p class="contact-phone">P. 800.214.5830</p>
        </div>
        <address class="office-address">
          27 Pellow Road<br>
          #09-04 Corbell Tower<br>
          Singapore 058214
        </address>
      </div>
      <div class="divider"></div>
      <div class="brand-panel">
        <div class="wordmark"><span>trizvo</span><span class="wordmark-dot"></span></div>
        <p class="website">www.trizvo.com</p>
      </div>
    </section>
  </main>
</body>
</html>
```